Nice craft box with banderole or sticker

We want to get a packaging box design for the 3D puzzle. The packaging is craft paper print black or white, wrap with a banderole or wrap with a stikcer. This box should be designed in a minimalist style as much as possible, as shown in the attached file. Only the product photos are in color, and the colors of the box and packaging are relatively simple. The color of the banderole or adhesive should be suitable. Products of different colors can be placed on without conflict. If you have better ideas, it's also possible. our product name is 3D paper puzzle or 3D cardboard Model. it have animal puzzles, like birds, insect ,wild animal. it is for young chirdren. 5-12 years old. the design also can be similar as our file, but it should be better than it.

The box size is about : 12*19*1.2CM, Attach is some packing design ideal and our logo.
we like nice font for the text. and 1-3 nice icon.

We like more nice design. It can attract the eyes. We hope all items can be use same banderole, and just put different animal photo on it.

Also You can visit our website: www.velmaro.com. you can kow how about our product.

We attach 3 items photo. You can choose one to make the design. Our product is DIY, education. Animal with scene

Target Market(s)

Europe,Janpan,USA

Requirements
Must have
• Text is black for the craft box. nice color for the banderole or sticker.
Nice to have
• nice icon.
Should not have
• craft box should not be very colorful.

```html
<!DOCTYPE html>
<html lang="en">
<head>
<meta charset="utf-8">
<title>3D Paper Puzzle – Orange Fox</title>
<link href="https://fonts.googleapis.com/css2?family=Fredoka:wght@500;600;700&family=Quicksand:wght@500;600;700&display=swap" rel="stylesheet">
<style>
  :root {
    --craft: #9c806a;
    --sand: #ead8c8;
    --ink: #141010;
    --cocoa: #3b2f27;
    --rule: #7d6652;
    --fox: #e05a28;
    --star: #7a6452;
    --paper: #ffffff;
  }
  * { margin: 0; padding: 0; box-sizing: border-box; }
  html, body { width: 758px; height: 1200px; overflow: hidden; }
  body { position: relative; background: var(--sand); font-family: "Quicksand", sans-serif; color: var(--cocoa); }

  .band-top { position: absolute; left: 0; top: 0; width: 758px; height: 663px; background: var(--craft); }
  .band-bottom { position: absolute; left: 0; top: 1105px; width: 758px; height: 95px; background: var(--craft); }

  .rule { position: absolute; left: 61px; width: 634px; height: 2px; background: var(--ink); }
  .rule--upper { top: 126px; }
  .rule--lower { top: 441px; }

  .headline {
    position: absolute; left: 0; width: 758px; text-align: center;
    font-family: "Fredoka", sans-serif; font-weight: 600; color: var(--ink); line-height: 1;
  }
  .headline--puzzle { top: 188px; font-size: 36px; }
  .headline--model { top: 340px; font-size: 44px; }

  .cube-row { position: absolute; left: 258px; top: 264px; }

  .feature { position: absolute; top: 473px; width: 140px; margin-left: -70px; text-align: center; }
  .feature svg { display: block; margin: 0 auto; }
  .feature__label { margin-top: 10px; font-family: "Fredoka", sans-serif; font-weight: 600; font-size: 16px; color: var(--ink); }
  .feature__dash { width: 32px; height: 2px; background: var(--ink); margin: 10px auto 0; }

  .product-photo {
    position: absolute; left: 63px; top: 726px; width: 316px; height: 316px; border-radius: 12px;
    background: radial-gradient(ellipse at 50% 40%, #f07a3e 0%, #f3a070 22%, #c9dc9a 42%, #ffffff 72%);
  }

  .info { position: absolute; left: 410px; top: 0; }
  .info__series { position: absolute; top: 744px; left: 0; white-space: nowrap; font-size: 25px; font-weight: 500; color: var(--cocoa); }
  .info__name { position: absolute; top: 772px; left: 0; white-space: nowrap; font-family: "Quicksand", sans-serif; font-weight: 700; font-size: 43px; color: var(--cocoa); letter-spacing: -0.5px; }
  .info__rule { position: absolute; top: 835px; left: 0; width: 348px; height: 2px; background: var(--rule); }
  .specs { position: absolute; top: 858px; left: 0; list-style: none; font-size: 16px; font-weight: 500; line-height: 26.5px; white-space: nowrap; color: var(--cocoa); }
  .specs strong { font-weight: 700; }
  .swatch { position: absolute; top: 972px; left: 1px; width: 47px; height: 47px; background: var(--fox); border: 2px solid var(--paper); }
  .difficulty { position: absolute; top: 977px; left: 63px; }
  .difficulty__label { font-size: 13px; font-weight: 500; color: var(--cocoa); }
  .difficulty__stars { display: block; margin-top: 4px; }
  .info__dashes { position: absolute; top: 1040px; left: 0; width: 285px; border-top: 2px dashed var(--rule); }

  .brand {
    position: absolute; left: 0; top: 1129px; width: 758px; text-align: center;
    font-family: "Fredoka", sans-serif; font-weight: 700; font-size: 36px; letter-spacing: 4px; color: var(--ink); line-height: 1;
  }
</style>
</head>
<body>
  <div class="band-top"></div>

  <div class="rule rule--upper"></div>
  <h1 class="headline headline--puzzle">3D Paper Puzzle</h1>

  <svg class="cube-row" width="242" height="52" viewBox="0 0 242 52" aria-hidden="true">
    <g fill="none" stroke="#141010" stroke-width="4" stroke-linejoin="round">
      <g transform="translate(25 26)"><path d="M0-22 19-11 19 11 0 22-19 11-19-11Z"/><path d="M-19-11 0 0 19-11M0 0V22"/></g>
      <g transform="translate(121 26)"><path d="M0-22 19-11 19 11 0 22-19 11-19-11Z"/><path d="M-19-11 0 0 19-11M0 0V22"/></g>
      <g transform="translate(217 26)"><path d="M0-22 19-11 19 11 0 22-19 11-19-11Z"/><path d="M-19-11 0 0 19-11M0 0V22"/></g>
    </g>
    <circle cx="73" cy="26" r="5" fill="#141010"/>
    <circle cx="169" cy="26" r="5" fill="#141010"/>
  </svg>

  <h2 class="headline headline--model">Cardboard Model</h2>
  <div class="rule rule--lower"></div>

  <div class="feature" style="left:168px">
    <svg width="50" height="50" viewBox="0 0 50 50" aria-hidden="true">
      <circle cx="25" cy="25" r="23" fill="none" stroke="#141010" stroke-width="2.5"/>
      <path d="M16 19h5a4 4 0 1 1 8 0h5v6a4 4 0 1 0 0 8v2h-6a4 4 0 1 0-8 0h-4v-6a4 4 0 1 1 0-8z" fill="none" stroke="#141010" stroke-width="2.2" stroke-linejoin="round"/>
    </svg>
    <div class="feature__label">Do It Yourself</div>
    <div class="feature__dash"></div>
  </div>

  <div class="feature" style="left:379px">
    <svg width="50" height="50" viewBox="0 0 50 50" aria-hidden="true">
      <circle cx="25" cy="25" r="23" fill="none" stroke="#141010" stroke-width="2.5"/>
      <path d="M16 34c0-11 7-18 19-18 0 12-7 18-16 17" fill="none" stroke="#141010" stroke-width="2.2" stroke-linejoin="round"/>
      <path d="M14 36 27 23" stroke="#141010" stroke-width="2.2" stroke-linecap="round"/>
    </svg>
    <div class="feature__label">Eco-Friendly</div>
    <div class="feature__dash"></div>
  </div>

  <div class="feature" style="left:589px">
    <svg width="50" height="50" viewBox="0 0 50 50" aria-hidden="true">
      <circle cx="25" cy="25" r="23" fill="none" stroke="#141010" stroke-width="2.5"/>
      <g fill="none" stroke="#141010" stroke-width="2.2" stroke-linecap="round">
        <circle cx="16" cy="24" r="3"/><circle cx="21" cy="32" r="3"/>
        <path d="M18 26 35 24M23 30 28 13"/>
        <path d="M9 41 41 9"/>
      </g>
    </svg>
    <div class="feature__label">Tool-Free</div>
    <div class="feature__dash"></div>
  </div>

  <div class="product-photo" role="img" aria-label="Photo of the assembled orange cardboard fox running over a green grass base, with loose puzzle pieces scattered below"></div>

  <div class="info">
    <p class="info__series">Animal Series</p>
    <h3 class="info__name">Orange Fox</h3>
    <div class="info__rule"></div>
    <ul class="specs">
      <li>Pieces: <strong>45 pcs</strong></li>
      <li>Size: 7x10 cm</li>
      <li>Material: Paper Cardboard</li>
      <li>Color: Orange</li>
    </ul>
    <div class="swatch"></div>
    <div class="difficulty">
      <div class="difficulty__label">Difficulty</div>
      <svg class="difficulty__stars" width="100" height="18" viewBox="0 0 100 18" aria-label="Difficulty 3 of 5">
        <defs><path id="star" d="M9 1l2.4 5 5.4.7-4 3.8 1 5.4L9 13.3 4.2 15.9l1-5.4-4-3.8L6.6 6z"/></defs>
        <use href="#star" x="0" fill="#7a6452"/>
        <use href="#star" x="20" fill="#7a6452"/>
        <use href="#star" x="40" fill="#7a6452"/>
        <use href="#star" x="60" fill="none" stroke="#7a6452" stroke-width="1.3"/>
        <use href="#star" x="80" fill="none" stroke="#7a6452" stroke-width="1.3"/>
      </svg>
    </div>
    <div class="info__dashes"></div>
  </div>

  <div class="band-bottom"></div>
  <div class="brand">VELMARO</div>
</body>
</html>
```